Awesome Professional Template for a collaborative report

File format: A4 PDF ideally

Design Requirements:

3 or 4 variants of a template some with graphics and pull quotes and a bio page for the essayists with a profile pic and a short descriptor

Layout Format: PPT would be perfect ideally portrait format

Style/Reference Guide: Varnholt or QM styles thought leadership reports as a guide

We need to input 10 essays around a specific subject with a nice layout with place holders for high impact pull quotes from the copy, stunning colourway and typrography probably A4 format but emailed as a PDF ideally not a huge file size. Striking front cover with title and list of contributors plus layout variations for the essays which will include a head shot short profile and contacts for the authors. Ideally a portrait format PPT that is easy to work with.

Target Market(s)

business professionals in brands

Industry/Entity Type

brand marketing

Font styles to use
Sans Serif

Colors
0054AA
0677BA
7BADD7
CADEEF
E8F1F8
00AB8E
00BBA5
67D7C9
C6EFE9
E9F9F6
F0912C
F2A743
F7CA91
FBE8D2
FDF5EE
6B429C
8869AF
B7A5CE
E3DAEB
F3F0F8

Requirements
Must have
• awesome visual impact

```html
<!DOCTYPE html>
<html lang="en">
<head>
<meta charset="utf-8">
<title>The Truth About New AI — Essay 01</title>
<link rel="stylesheet" href="https://fonts.googleapis.com/css2?family=IBM+Plex+Sans:ital,wght@0,300;0,400;0,600;0,700;1,400&display=swap">
<style>
  :root {
    --paper: #ffffff;
    --ink: #0b1a3c;
    --night: #060b30;
    --night-soft: #081538;
    --night-deep: #040826;
    --violet: #4b2a7b;
    --violet-rule: #4a2c82;
    --cyan: #4fc3d9;
    --text-light: #ffffff;
    --text-muted: #e1e5ef;
  }
  * { margin: 0; padding: 0; box-sizing: border-box; }
  html, body { width: 845px; height: 1200px; overflow: hidden; background: var(--paper); }
  body { font-family: "IBM Plex Sans", Arial, sans-serif; }

  .cover { position: relative; width: 845px; height: 1200px; overflow: hidden; background: var(--paper); }

  .cover__night {
    position: absolute; left: 0; top: 438px; width: 845px; height: 762px;
    background: linear-gradient(180deg, var(--night-soft) 0%, var(--night) 60%, var(--night-deep) 100%);
  }

  .cover__art { position: absolute; left: 0; top: 0; width: 845px; height: 1200px; }

  .issue-number {
    position: absolute; left: 75px; top: 90px;
    font-size: 70px; font-weight: 600; letter-spacing: -2px; color: var(--ink); line-height: 1;
  }
  .issue-page {
    position: absolute; left: 82px; top: 176px;
    font-size: 24px; font-weight: 400; color: var(--cyan); line-height: 1;
  }
  .issue-date {
    position: absolute; left: 80px; top: 406px;
    transform: rotate(-90deg); transform-origin: left top;
    font-size: 12px; font-weight: 400; color: var(--ink); letter-spacing: 0.5px; white-space: nowrap;
  }

  .essay-head { position: absolute; left: 76px; top: 816px; width: 405px; color: var(--text-light); }
  .series { font-size: 15px; font-weight: 400; padding-bottom: 7px; border-bottom: 2px solid var(--violet-rule); }
  .series strong { font-weight: 700; }
  .series em { font-style: italic; margin-left: 6px; }

  .essay-title { margin-top: 24px; font-weight: 300; font-size: 20px; line-height: 1.08; padding-left: 3px; }
  .essay-title__impact {
    display: block; margin-top: 6px; margin-left: -3px;
    font-size: 34px; font-weight: 700; letter-spacing: 0.2px; line-height: 1.1;
  }
  .essay-rule { margin-top: 22px; height: 5px; background: var(--violet-rule); width: 403px; }

  .author { margin-top: 11px; }
  .author__name { font-size: 16.5px; font-weight: 600; line-height: 1.2; }
  .author__role { font-size: 11.5px; font-weight: 300; color: var(--text-muted); }

  .teaser {
    position: absolute; right: 104px; top: 1099px; width: 300px;
    text-align: right; color: var(--text-muted);
    font-size: 11.5px; line-height: 16px; font-weight: 400;
  }
  .teaser__bar { position: absolute; left: 757px; top: 1090px; width: 8px; height: 68px; background: var(--violet-rule); }
</style>
</head>
<body>
  <main class="cover">
    <div class="cover__night"></div>

    <svg class="cover__art" viewBox="0 0 845 1200" width="845" height="1200">
      <defs>
        <linearGradient id="portraitTone" x1="0" y1="0" x2="0" y2="1">
          <stop offset="0" stop-color="#1fb4ea" stop-opacity="0.9"/>
          <stop offset="0.5" stop-color="#1766b4" stop-opacity="0.75"/>
          <stop offset="1" stop-color="#1c2a72" stop-opacity="0.6"/>
        </linearGradient>
      </defs>
      <circle class="backdrop-sweep" cx="240" cy="1320" r="690" fill="#050a2b" opacity="0.75"/>
      <circle class="backdrop-sweep" cx="60" cy="1160" r="190" fill="#04071f" opacity="0.6"/>

      <path class="ring-arc" d="M 288 425 A 304 304 0 0 0 779 664"
            fill="none" stroke="var(--cyan)" stroke-width="34"/>
      <circle class="ring" cx="591" cy="438" r="271" fill="var(--violet)"/>
      <circle class="ring-core" cx="591" cy="438" r="180" fill="#06163a"/>

      <rect class="feature-image" role="img"
            aria-label="Feature illustration: low-poly digital human head in blue tones with network lines, symbolising artificial intelligence"
            x="430" y="118" width="326" height="458" fill="url(#portraitTone)"/>
    </svg>

    <div class="issue-number">01</div>
    <div class="issue-page">15</div>
    <div class="issue-date">JUL 2023</div>

    <section class="essay-head">
      <p class="series">The Truth About <strong>NEW AI</strong><em>(collaborative series)</em></p>
      <h1 class="essay-title">
        The Short &amp; Concise Essay<br>Title Should Go Here, Adding a Bold
        <span class="essay-title__impact">IMPACT PHRASE HERE</span>
      </h1>
      <div class="essay-rule"></div>
      <div class="author">
        <p class="author__name">Charles van Vengeance</p>
        <p class="author__role">Job Title, FillInCorp Ltd</p>
      </div>
    </section>

    <p class="teaser">Add a powerful teaser or description here. Lorem<br>ipsum dolor sit amet, consectetur adipiscing elit.<br>Vivamus euismod venenatis aliquam.</p>
    <div class="teaser__bar"></div>
  </main>
</body>
</html>
```